property investment and development company needs a website

we need a website that looks professional and portrays trust for people looking to us to buy their house or investors looking to invest or joint venture with us.
We are based in the west midlands in the UK.
we deal mainly with residential housing, house to flats conversions, HMO's (houses in multiple ocupancy).
we require the website as a first point of contact with potential sellers, renters and investors so links or contact details that are easy to access or see would be good.
I have had logos designed by a plan hollow member and these can be used as guidance for the colour and style of the site.
Target Market(s)
joint venture investment partners, people looking to sell their house, people looking to rent from us.
Coding
Coded - Design and coding required
Number of Pages Required
3 page
Requirements
Must have
- project a professional appearance
- visable contact details

```html
<!DOCTYPE html>
<html lang="en">
<head>
<meta charset="utf-8">
<title>Harlow Homes — Property Development &amp; Investment</title>
<link rel="stylesheet" href="https://fonts.googleapis.com/css2?family=Cinzel:wght@400;600;700&family=Lora:wght@400&family=Roboto:wght@300;400&display=swap">
<style>
:root{
  --navy:#252c3b;
  --gold:#c8902a;
  --gold-light:#d9a443;
  --grey:#efefef;
  --text:#3a3a3a;
  --muted:#555;
  --line:#d6d6d6;
}
*{box-sizing:border-box;margin:0;padding:0}
html,body{width:1200px;height:4427px;overflow:hidden}
body{position:relative;background:#fff;font-family:"Lora",serif;color:var(--text)}
.abs{position:absolute}
.cinzel{font-family:"Cinzel",serif}

/* header */
.topbar{left:0;top:0;width:1200px;height:148px;background:var(--navy)}
.top-contact{top:50px;display:flex;align-items:center;gap:12px;color:#e8e8e8;font-family:"Cinzel",serif;font-size:14px;line-height:22px}
.brand{font-family:"Cinzel",serif;font-weight:600;color:var(--gold-light);line-height:1}
.main-nav{left:0;top:148px;width:1200px;height:60px;background:#fff;display:flex;justify-content:center;align-items:center;gap:44px;font-family:"Cinzel",serif;font-weight:700;font-size:17px;color:var(--navy)}

/* hero */
.hero{left:0;top:208px;width:1200px;height:628px;background:linear-gradient(180deg,#6f6f6c 0%,#9a9791 45%,#bdb9b2 75%,#8c8a86 100%)}
.hero-title{left:700px;top:258px;color:#fff;font-family:"Cinzel",serif;line-height:1.1}

/* services */
.card{top:914px;width:323px;height:284px;border:1px solid #cfcfcf;background:#fff;padding:0 22px}
.card h3{position:absolute;top:133px;left:24px;font-family:"Cinzel",serif;font-weight:600;font-size:16px;color:var(--navy)}
.card p{position:absolute;top:165px;left:20px;right:20px;font-size:13.5px;line-height:31px;text-align:justify;color:var(--muted)}
.card svg{position:absolute;left:24px;top:70px}

/* sections */
.band{left:0;width:1200px}
.sec-title{font-family:"Cinzel",serif;font-weight:600;font-size:41px;color:var(--gold)}
.sec-text{font-size:13.5px;line-height:35.5px;text-align:justify;color:var(--text)}
.photo{box-shadow:0 4px 18px rgba(0,0,0,.18)}

/* contact */
.info-ico{width:86px;height:86px;border-radius:50%;background:var(--navy);display:flex;align-items:center;justify-content:center}
.info-txt{font-family:"Cinzel",serif;font-size:17px;line-height:28px;text-align:center;color:#4a4a4a}
.info-txt b{color:var(--gold);font-weight:600;display:block}
.field{height:38px;background:#fff;border:1px solid #e4e4e4;box-shadow:0 1px 4px rgba(0,0,0,.08);font-family:"Roboto",sans-serif;font-size:12px;color:#555;padding:12px 0 0 18px}
.submit{left:511px;top:3980px;width:178px;height:48px;background:linear-gradient(#d5a24a,#c08a2d);color:#fff;font-family:"Cinzel",serif;font-weight:700;font-size:16px;display:flex;align-items:center;justify-content:center;gap:10px}

/* footer */
.footer{left:0;top:4105px;width:1200px;height:322px;background:var(--navy)}
.social{top:4297px;width:28px;height:28px;border:2px solid #fff;border-radius:50%}
.foot-nav{left:0;top:4346px;width:1200px;display:flex;justify-content:center;gap:14px;font-family:"Cinzel",serif;font-weight:700;font-size:17px;color:#fff}
.copy{left:0;top:4386px;width:1200px;text-align:center;font-family:"Roboto",sans-serif;font-size:14px;color:#ddd}
</style>
</head>
<body>

<!-- header -->
<div class="abs topbar"></div>
<div class="abs top-contact" style="left:155px">
  <svg width="40" height="40" viewBox="0 0 40 40"><circle cx="20" cy="20" r="17" fill="none" stroke="#e0a23a" stroke-width="2.5"/><path d="M14 12c2-1 3 3 4 4s-2 2-1 4 3 4 4 4 2-3 3-2 4 3 3 4c-2 3-5 3-9 0s-7-8-6-11c0-1 1-2 2-3z" fill="#e0a23a"/></svg>
  <div>CALL US:<br>07700 900418</div>
</div>
<div class="abs brand" style="left:545px;top:30px;font-size:44px;text-align:left">HARLOW<br>HOMES</div>
<div class="abs top-contact" style="left:810px">
  <svg width="56" height="38" viewBox="0 0 56 38"><rect x="1" y="1" width="54" height="36" fill="#e0a23a"/><path d="M1 1l27 20L55 1" fill="none" stroke="#252c3b" stroke-width="2"/><path d="M1 37l20-18M55 37L35 19" stroke="#252c3b" stroke-width="2"/></svg>
  <div>MAIL US:<br>INFO@HARLOWHOMES.EXAMPLE</div>
</div>

<nav class="abs main-nav">
  <span>HOME</span><span>ABOUT US</span><span>SELL</span><span>INVEST</span><span>CONTACT US</span>
  <span style="display:flex;align-items:center;gap:8px">SEARCH <svg width="16" height="16" viewBox="0 0 16 16"><circle cx="6.5" cy="6.5" r="5" fill="none" stroke="#252c3b" stroke-width="2.2"/><path d="M10 10l5 5" stroke="#252c3b" stroke-width="2.5"/></svg></span>
</nav>

<!-- hero -->
<div class="abs hero" role="img" aria-label="Bright loft living room with tall steel-framed windows, pendant lamps and grey sofa"></div>
<div class="abs hero-title">
  <div style="font-size:35px">WELCOME TO</div>
  <div style="font-size:54px;margin-top:8px">HARLOW HOMES</div>
</div>
<svg class="abs" style="left:0;top:776px" width="1200" height="62" viewBox="0 0 1200 62"><path d="M420 62C500 62 520 14 600 14S700 62 780 62Z" fill="#fff"/><path d="M590 46l8-8 8 8" fill="none" stroke="#333" stroke-width="2"/></svg>

<!-- services -->
<div class="abs card" style="left:93px">
  <svg width="62" height="48" viewBox="0 0 62 48"><path d="M31 2L2 26h8v20h16V32h10v14h16V26h8z" fill="#d9822b"/></svg>
  <h3>RESIDENTIAL HOUSING</h3>
  <p>At vero eos et accusamus et iusto odio dignissimos ducimus qui blanditiis praesentium voluptatum</p>
</div>
<div class="abs card" style="left:442px">
  <svg width="52" height="52" viewBox="0 0 52 52" fill="none" stroke="#d9822b" stroke-width="2"><rect x="8" y="2" width="36" height="48"/><path d="M14 10h24M14 18h24M14 26h24M14 34h24M2 50h48"/><rect x="20" y="40" width="12" height="10"/></svg>
  <h3>HOUSE TO FLATS CONVERSIONS</h3>
  <p>At vero eos et accusamus et iusto odio dignissimos ducimus qui blanditiis praesentium voluptatum</p>
</div>
<div class="abs card" style="left:791px">
  <svg width="52" height="52" viewBox="0 0 52 52" fill="none" stroke="#d9822b" stroke-width="2"><rect x="14" y="2" width="26" height="48"/><rect x="2" y="20" width="12" height="30"/><path d="M20 10h4M30 10h4M20 18h4M30 18h4M20 26h4M30 26h4M20 34h4M30 34h4M6 28h4M6 36h4M42 50h8"/></svg>
  <h3>HMO'S</h3>
  <p>At vero eos et accusamus et iusto odio dignissimos ducimus qui blanditiis praesentium voluptatum</p>
</div>

<!-- about -->
<div class="abs band" style="top:1277px;height:674px;background:var(--grey)"></div>
<h2 class="abs sec-title" style="left:89px;top:1472px">ABOUT US</h2>
<div class="abs sec-text" style="left:89px;top:1547px;width:452px">
  <p>We are a property development and investment company that have our own portfolio and we are active investors who pride ourselves in expanding our business organically.</p>
  <p>We ensure that whatever your property needs are we deliver bespoke services for our clients. For investors, sellers, landlords and tenants we bring knowledge to your next property decision, allowing you to make an informed decision.</p>
</div>
<div class="abs" style="left:679px;top:1356px;width:521px;height:520px;background:linear-gradient(135deg,#5f7a4a,#8a9a7a 40%,#6a8356)" role="img" aria-label="Aerial view of a suburban street with houses and trees"></div>
<div class="abs photo" style="left:593px;top:1425px;width:476px;height:382px;background:linear-gradient(160deg,#6d8552,#9aa08c 45%,#587245)" role="img" aria-label="Tilt-shift aerial view of a residential neighbourhood"></div>

<!-- invest -->
<div class="abs" style="left:0;top:2027px;width:516px;height:519px;background:linear-gradient(120deg,#e8b444,#b9904a 45%,#6d5a3e)" role="img" aria-label="Hands working at a desk with a laptop, papers and calculator in warm light"></div>
<div class="abs photo" style="left:131px;top:2095px;width:476px;height:384px;background:linear-gradient(135deg,#f2c55a,#d8b579 40%,#a8977a 75%,#8d7c62)" role="img" aria-label="Close view of hands reviewing documents beside a laptop"></div>
<h2 class="abs sec-title" style="left:662px;top:2083px">INVEST</h2>
<div class="abs sec-text" style="left:662px;top:2155px;width:440px;line-height:31.3px">
  <p>We have our own portfolio and we are active investors, so our finger is on the pulse and we are currently looking for residential development investments &amp;amp; commercial to residential conversions in cities or regional centres showing strong growth.</p>
  <p>Our experience in the industry enables us to make extremely quick and well-informed decisions. We follow the opportunities that are presented to us as well as sourcing opportunities ourselves. We are happy to work in partnership and within joint ventures and have a proven track record of establishing excellent relationships in these areas.</p>
</div>

<!-- sell -->
<div class="abs band" style="top:2622px;height:675px;background:var(--grey)"></div>
<h2 class="abs sec-title" style="left:93px;top:2757px">SELL</h2>
<div class="abs sec-text" style="left:93px;top:2829px;width:442px;line-height:31.3px">
  <p>We undertake the necessary market research to evaluate an option that works for all parties involved. We will help guide you to make an informed decision on how to gain the maximum realistic value.</p>
  <p>For those looking to achieve a fast and professional sale to experienced investors, we provide an approach that has been proven to work for many others.</p>
  <p>If you would like to discuss a property you are looking to sell, then please contact us on 01632 960512</p>
</div>
<div class="abs" style="left:679px;top:2699px;width:521px;height:521px;background:linear-gradient(135deg,#9fb2c2,#c9d3db 50%,#7f94a6)" role="img" aria-label="Bright interior of a new home"></div>
<div class="abs photo" style="left:588px;top:2769px;width:476px;height:382px;background:linear-gradient(135deg,#5f7e9e,#b6c4d1 45%,#46627f)" role="img" aria-label="Happy couple receiving the keys to their new home"></div>

<!-- contact -->
<h2 class="abs sec-title" style="left:0;top:3362px;width:1200px;text-align:center;font-size:36px">CONTACT INFORMATION</h2>
<div class="abs" style="left:0;top:3424px;width:1200px;text-align:center;font-family:'Roboto',sans-serif;font-weight:300;font-size:23px;color:#444">Contact us for more information</div>

<div class="abs info-ico" style="left:260px;top:3483px"><svg width="40" height="48" viewBox="0 0 40 48" fill="none" stroke="#fff" stroke-width="2"><path d="M20 44S6 28 6 18a14 14 0 0128 0c0 10-14 26-14 26z"/><circle cx="20" cy="18" r="5"/><ellipse cx="20" cy="44" rx="14" ry="3"/></svg></div>
<div class="abs info-ico" style="left:555px;top:3483px"><svg width="40" height="40" viewBox="0 0 40 40" fill="none" stroke="#fff" stroke-width="2"><path d="M8 4c3-2 5 5 7 7s-3 4-2 6 6 9 9 10 4-4 6-3 8 4 7 7c-3 6-9 6-16 1S5 19 4 12c0-3 2-6 4-8z"/></svg></div>
<div class="abs info-ico" style="left:872px;top:3483px"><svg width="44" height="32" viewBox="0 0 44 32" fill="none" stroke="#fff" stroke-width="2"><rect x="2" y="2" width="40" height="28"/><path d="M2 2l20 16L42 2M2 30l15-14M42 30L27 16"/></svg></div>

<div class="abs info-txt" style="left:143px;top:3582px;width:320px">12 Fernbrook Lane, Ledwell,<br>Westshire, WS9 4QT</div>
<div class="abs info-txt" style="left:450px;top:3582px;width:300px"><b>PHONE:</b>07700 900418</div>
<div class="abs info-txt" style="left:745px;top:3582px;width:340px"><b>EMAIL:</b>INFO@HARLOWHOMES.EXAMPLE</div>

<h2 class="abs sec-title" style="left:0;top:3693px;width:1200px;text-align:center;font-size:36px">CONTACT US</h2>

<div class="abs field" style="left:162px;top:3761px;width:428px">&#128100; First Name</div>
<div class="abs field" style="left:612px;top:3761px;width:426px">&#128100; Last Name</div>
<div class="abs field" style="left:162px;top:3816px;width:428px">&#9646; Company</div>
<div class="abs field" style="left:612px;top:3816px;width:426px;height:150px">&#128172; Message :</div>
<div class="abs field" style="left:162px;top:3869px;width:428px">&#9993; Email Address</div>
<div class="abs field" style="left:162px;top:3924px;width:428px">&#9742; Phone Number</div>
<div class="abs submit"><svg width="18" height="18" viewBox="0 0 18 18"><path d="M1 8l16-7-5 16-3-6z" fill="#fff"/></svg>SUBMIT</div>

<!-- footer -->
<div class="abs footer"></div>
<div class="abs brand" style="left:0;top:4150px;width:1200px;text-align:center;font-size:56px;line-height:62px">HARLOW<br>HOMES</div>
<div class="abs social" style="left:531px"></div>
<div class="abs social" style="left:567px"></div>
<div class="abs social" style="left:603px"></div>
<div class="abs social" style="left:639px"></div>
<div class="abs foot-nav"><span>HOME</span><span>|</span><span>ABOUT US</span><span>|</span><span>INVEST</span><span>|</span><span>SELL</span><span>|</span><span>CONTACT US</span></div>
<div class="abs copy">© 2019 Company Name &nbsp;All right reserved</div>

</body>
</html>
```